" **Briefing para Desenvolvimento de Logotipo - Velmira** **1. Conceito da Marca:** - A Velmira tem como essência o conceito de "Arte Aplicada ao Corpo." A marca posiciona seus profissionais como "artistas corporais" e enxerga cada tratamento como uma forma de escultura. - A missão é transformar e esculpir o corpo de cada cliente com a mesma dedicação e precisão de um artista com sua obra de arte, valorizando a beleza única de cada indivíduo. **2. Personalização e Exclusividade:** - Cada cliente é uma “obra única,” e a Velmira se compromete a oferecer tratamentos personalizados, “sob medida.” O logotipo deve comunicar esse nível de exclusividade e atenção individual, remetendo à ideia de que cada pessoa é um projeto único e especial. **3. Transformação e Metamorfose:** - A Velmira trabalha com a ideia de transformação, tal como um escultor que molda o “bloco de mármore” em uma escultura. Esta visão deve transparecer no logotipo, talvez através de elementos que remetam à progressão e ao desenvolvimento de uma obra. **4. Expertise e Precisão:** - A equipe da Velmira é composta por “mestres escultores” que dedicam cuidado, precisão e técnica em cada tratamento. O logotipo deve reforçar essa expertise e compromisso com a excelência. **5. Inovação e Vanguarda:** - A marca busca ser reconhecida pela inovação, sempre apresentando novos tratamentos e posicionando-se na vanguarda da “arte corporal.” O design do logotipo deve refletir uma estética moderna e refinada que comunique tecnologia e evolução no cuidado corporal. **6. Experiência do Cliente:** - A clínica proporciona uma atmosfera similar a um “ateliê de arte,” oferecendo consultas personalizadas como “sessões criativas” entre cliente e artista corporal. Deseja-se que o logotipo transmita essa sensação acolhedora e artística. **7. Identidade Visual e Inspiração:** - A identidade visual da Velmira deve ser inspirada em esculturas clássicas, talvez incorporando elementos que remetam a formas humanas e artísticas. - O logotipo pode utilizar linhas suaves e orgânicas, texturas que lembrem mármore ou pedra, sugerindo uma conexão entre o corpo e a arte. **8. Aplicações e Comunicação Visual:** - O logotipo deve ser versátil para aplicação em diferentes materiais e plataformas, incluindo papelaria, redes sociais, uniformes e sinalização da clínica. - As cores devem refletir a sofisticação e a exclusividade da marca, buscando um equilíbrio entre tons clássicos e modernos. **9. Campanhas e Relação com a Comunidade Artística:** - A Velmira planeja lançar uma série de campanhas chamadas “O Voo da Lua,” mostrando o processo de transformação dos clientes. A marca também visa colaborar com artistas locais para conteúdos que integrem o conceito de arte ao corpo humano. - O logotipo deve se conectar com essas iniciativas, possibilitando uma fácil integração com elementos de design para campanhas artísticas e eventos. **10. Programa de Fidelização:** - O programa de fidelidade “Guardião do Farol” deve ser representado no design de forma que remeta a exclusividade e à ideia de um cliente que coleciona experiências e melhorias na sua estética ao longo do tempo. Esse briefing visa orientar o desenvolvimento de um logotipo que represente o DNA da Velmira, explorando o conceito de corpo como arte, alinhando precisão, inovação e personalização. "

```html
<!DOCTYPE html>
<html lang="pt-BR">
<head>
<meta charset="utf-8">
<title>Velmira — Cartões</title>
<link rel="stylesheet" href="https://fonts.googleapis.com/css2?family=Montserrat:wght@300;400&display=swap">
<style>
  :root {
    --page: #eeeeee;
    --ink: #0c0c0c;
    --paper: #ffffff;
    --gold: #c9a35f;
    --gold-deep: #8a6a35;
    --text-light: #f2f2f2;
    --text-dark: #3a3a3a;
  }
  * { box-sizing: border-box; margin: 0; padding: 0; }
  html, body { width: 1200px; height: 1200px; overflow: hidden; }
  body {
    background: var(--page);
    font-family: "Montserrat", sans-serif;
    position: relative;
  }
  .card {
    position: absolute;
    left: 180px;
    width: 840px;
    height: 480px;
    overflow: hidden;
    box-shadow: 0 6px 18px rgba(0,0,0,0.12);
  }
  .card--front { top: 90px; background: var(--ink); }
  .card--back { top: 630px; background: var(--ink); display: flex; }

  .body-art {
    position: absolute;
    right: 0; top: 0;
    width: 520px; height: 480px;
    background:
      radial-gradient(ellipse 60% 45% at 55% 50%, rgba(201,163,95,0.55), rgba(201,163,95,0.12) 60%, transparent 75%);
  }
  .body-art--faint {
    left: 0; right: auto;
    width: 100%;
    opacity: 0.35;
  }

  .brand {
    display: flex;
    align-items: center;
    gap: 16px;
  }
  .brand__mark {
    width: 54px; height: 54px;
    border: 2px solid var(--gold);
    border-radius: 50%;
    flex: none;
  }
  .brand__name {
    font-weight: 300;
    font-size: 58px;
    letter-spacing: 1px;
    line-height: 1;
  }
  .brand__tagline {
    font-weight: 300;
    font-size: 14px;
    letter-spacing: 2px;
    margin-top: 8px;
    margin-left: 72px;
  }

  .card--front .brand-block {
    position: absolute;
    left: 70px; bottom: 80px;
    color: var(--text-light);
  }

  .card__info {
    width: 300px;
    height: 100%;
    background: var(--paper);
    color: var(--text-dark);
    padding: 150px 30px 0 34px;
    position: relative;
    z-index: 1;
  }
  .card__info .brand__name { font-size: 44px; }
  .card__info .brand__mark { width: 42px; height: 42px; }
  .card__info .brand__tagline { font-size: 11px; margin-left: 58px; }
  .contact {
    list-style: none;
    margin-top: 60px;
    font-size: 12px;
    line-height: 1.9;
  }
  .contact li { display: flex; align-items: center; gap: 8px; }
  .contact svg { width: 11px; height: 11px; fill: var(--gold); flex: none; }

  .card__stamps {
    flex: 1;
    position: relative;
    display: grid;
    grid-template-columns: repeat(5, 72px);
    grid-template-rows: repeat(2, 72px);
    gap: 44px 30px;
    align-content: center;
    justify-content: center;
  }
  .stamp {
    width: 72px; height: 72px;
    border-radius: 50%;
    background: var(--paper);
    border: 4px solid var(--gold);
    position: relative;
    z-index: 1;
  }
</style>
</head>
<body>
  <section class="card card--front">
    <div class="body-art" role="img" aria-label="Ilustração em linhas douradas de uma silhueta corporal esculpida"></div>
    <div class="brand-block">
      <div class="brand">
        <span class="brand__mark"></span>
        <span class="brand__name">Velmira</span>
      </div>
      <p class="brand__tagline">O Voo da Lua</p>
    </div>
  </section>

  <section class="card card--back">
    <div class="card__info">
      <div class="brand">
        <span class="brand__mark"></span>
        <span class="brand__name">Velmira</span>
      </div>
      <p class="brand__tagline">O Voo da Lua</p>
      <ul class="contact">
        <li><svg viewBox="0 0 10 10"><circle cx="5" cy="5" r="5"/></svg>(11) 4000-2718</li>
        <li><svg viewBox="0 0 10 10"><circle cx="5" cy="5" r="5"/></svg>@velmira.estetica</li>
        <li><svg viewBox="0 0 10 10"><circle cx="5" cy="5" r="5"/></svg>www.velmira.com.br</li>
      </ul>
    </div>
    <div class="card__stamps">
      <div class="body-art body-art--faint" role="img" aria-label="Ilustração suave da silhueta corporal ao fundo"></div>
      <span class="stamp"></span><span class="stamp"></span><span class="stamp"></span><span class="stamp"></span><span class="stamp"></span>
      <span class="stamp"></span><span class="stamp"></span><span class="stamp"></span><span class="stamp"></span><span class="stamp"></span>
    </div>
  </section>
</body>
</html>
```